Generic Post Card

New Product promotion. Attached is a card we did earlier. I made modifications to it so you can get an idea of what I want. The colors match our web page at quorvelmist.com

Product

```html
<!DOCTYPE html>
<html lang="en">
<head>
<meta charset="utf-8">
<title>Nitrous Oxide Inhaler – Post Card</title>
<link rel="stylesheet" href="https://fonts.googleapis.com/css2?family=Open+Sans:wght@300;400;600;700&display=swap">
<style>
  :root {
    --brand-blue: #1d4a8c;
    --brand-blue-dark: #234887;
    --bar-blue-top: #1b3f86;
    --bar-blue-bottom: #1f86c8;
    --brand-orange: #f7931e;
    --orange-light: #fbb040;
    --orange-text: #f7901e;
    --cross-orange: #fdd3a1;
    --peach-band: #fdd5a0;
    --tagline-bg: #cfe3f5;
    --pill-blue: #27508c;
    --white: #ffffff;
    --product-tone: #e9eaeb;
    --portrait-tone: #b9c4bb;
  }
  * { margin: 0; padding: 0; box-sizing: border-box; }
  html, body { width: 1200px; height: 922px; overflow: hidden; background: var(--white); }
  body { font-family: "Open Sans", Arial, sans-serif; }

  .card { position: relative; width: 1200px; height: 922px; background: var(--white); overflow: hidden; }

  .top-bar { position: absolute; top: 0; height: 52px; }
  .top-bar--blue { left: 0; width: 464px; background: linear-gradient(180deg, var(--bar-blue-top), var(--bar-blue-bottom)); }
  .top-bar--orange { left: 471px; width: 729px; background: linear-gradient(180deg, var(--brand-orange), var(--orange-light)); }

  .headline {
    position: absolute; left: 32px; top: 68px;
    font-size: 70px; line-height: 1; letter-spacing: -1px; white-space: nowrap;
  }
  .headline__strong { color: var(--brand-blue); font-weight: 700; }
  .headline__light { color: var(--brand-orange); font-weight: 300; }

  .tagline {
    position: absolute; left: 464px; top: 158px; width: 736px; height: 79px;
    background: var(--tagline-bg); color: var(--brand-blue);
    font-size: 37px; font-weight: 400; line-height: 79px; padding-left: 19px; white-space: nowrap; letter-spacing: -0.5px;
  }
  .tagline strong { font-weight: 700; }

  .product-shot {
    position: absolute; left: 18px; top: 356px; width: 334px; height: 368px;
    background: linear-gradient(160deg, var(--product-tone), #d9dbdd);
    border-radius: 14px;
  }

  .equation-sign { position: absolute; }
  .equation-sign--plus { left: 368px; top: 508px; }
  .equation-sign--equals { left: 704px; top: 520px; }

  .procedure { position: absolute; left: 444px; top: 382px; width: 286px; height: 286px; }
  .procedure__cross { position: absolute; inset: 0; }
  .procedure__text {
    position: absolute; left: -20px; right: -20px; top: 50px;
    text-align: center; color: var(--orange-text); font-weight: 700;
    font-size: 46px; line-height: 66px; letter-spacing: -0.5px;
  }

  .patient-portrait {
    position: absolute; left: 808px; top: 280px; width: 344px; height: 518px;
    background: linear-gradient(180deg, #c9b9a8 0%, var(--portrait-tone) 40%, #9fb0a3 100%);
    border-radius: 150px 150px 20px 20px;
  }
  .patient-badge {
    position: absolute; left: 864px; top: 708px; width: 246px; height: 42px;
    background: var(--pill-blue); color: var(--white); border-radius: 21px;
    font-size: 24px; font-weight: 700; text-align: center; line-height: 42px; letter-spacing: -0.3px;
  }

  .peach-band { position: absolute; left: 0; top: 804px; width: 1200px; height: 38px; background: var(--peach-band); }
  .footer-bar {
    position: absolute; left: 0; top: 848px; width: 1200px; height: 74px;
    background: var(--brand-blue-dark); color: var(--white);
    font-size: 33px; font-weight: 400; text-align: center; line-height: 74px;
  }
</style>
</head>
<body>
<main class="card">
  <div class="top-bar top-bar--blue"></div>
  <div class="top-bar top-bar--orange"></div>

  <h1 class="headline"><span class="headline__strong">Nitrous Oxide</span> <span class="headline__light">Inhaler</span></h1>

  <p class="tagline">Reduced <strong>PAIN</strong> &amp; <strong>ANXIETY</strong> in seconds</p>

  <div class="product-shot" role="img" aria-label="Photo of the white hand-held nitrous oxide inhaler device"></div>

  <svg class="equation-sign equation-sign--plus" width="50" height="50" viewBox="0 0 50 50" aria-hidden="true">
    <rect x="22" y="0" width="5" height="50" fill="var(--brand-blue)"/>
    <rect x="0" y="22.5" width="49" height="5" fill="var(--brand-blue)"/>
  </svg>

  <div class="procedure">
    <svg class="procedure__cross" width="286" height="286" viewBox="0 0 286 286" aria-hidden="true">
      <line x1="0" y1="0" x2="286" y2="286" stroke="var(--cross-orange)" stroke-width="4"/>
      <line x1="286" y1="0" x2="0" y2="286" stroke="var(--cross-orange)" stroke-width="4"/>
    </svg>
    <p class="procedure__text">Your<br>Painful<br>Procedure</p>
  </div>

  <svg class="equation-sign equation-sign--equals" width="46" height="27" viewBox="0 0 46 27" aria-hidden="true">
    <rect x="0" y="0" width="46" height="5" fill="var(--brand-blue)"/>
    <rect x="0" y="22" width="46" height="5" fill="var(--brand-blue)"/>
  </svg>

  <div class="patient-portrait" role="img" aria-label="Photo of a smiling patient with arms crossed"></div>
  <div class="patient-badge">Happy Patient</div>

  <div class="peach-band"></div>
  <footer class="footer-bar">Ask your nurse for availability and pricing.</footer>
</main>
</body>
</html>
```